New legal process in family law needs graphic for home page of website

The new startup is called the Bluegum Accord in Australia. The idea is to offer a way of solving family law disputes by offering mediation and arbitration. That’s why it is an bluegum accord – it is an alternative to the courts.
We need to encourage lawyers to refer clients to the service rather than going to court, so I would like a homepage graphic which is bright and interesting, and suggests to lawyers that this is a more sensible way of resolving family law disputes than spending a couple of years stuck in the court system.

Target Market(s)

Lawyers, family law clients

Industry/Entity Type

Family Law

Font styles to use
Serif
Sans Serif

Requirements
Nice to have
• My logo is uploaded below.

```html
<!DOCTYPE html>
<html lang="en">
<head>
<meta charset="utf-8">
<title>Bluegum Accord – Mediation and Arbitration</title>
<link rel="stylesheet" href="https://fonts.googleapis.com/css2?family=Dosis:wght@500;600&family=Raleway:wght@500&display=swap">
<style>
  :root {
    --cream-light: #fbf3d6;
    --cream-mid: #f1e2ad;
    --cream-deep: #e2cd8c;
    --ink: #1f1f1f;
    --accent-blue: #2e8ab8;
    --ring-blue: #2b8cb6;
    --nav-grey: #3f4145;
    --white: #ffffff;
    --photo-light: #ece6df;
    --photo-mid: #d6cbbd;
    --photo-warm: #b7926a;
  }
  html, body {
    margin: 0;
    padding: 0;
    overflow: hidden;
  }
  .hero-banner {
    position: relative;
    width: 1200px;
    height: 450px;
    overflow: hidden;
    background: linear-gradient(100deg, var(--cream-light) 0%, var(--cream-mid) 45%, var(--cream-deep) 100%);
  }
  .decor-circle {
    position: absolute;
    left: 70px;
    top: 95px;
    width: 280px;
    height: 280px;
    border-radius: 50%;
    background: rgba(140, 190, 175, 0.14);
  }
  .hero-copy {
    position: absolute;
    left: 95px;
    top: 110px;
    width: 360px;
  }
  .hero-headline {
    margin: 0;
    font-family: "Dosis", sans-serif;
    font-weight: 500;
    font-size: 34px;
    line-height: 47px;
    color: var(--ink);
  }
  .cta-button {
    display: inline-flex;
    align-items: center;
    justify-content: center;
    margin-top: 12px;
    width: 217px;
    height: 51px;
    background: var(--accent-blue);
    color: var(--white);
    font-family: "Raleway", sans-serif;
    font-weight: 500;
    font-size: 29px;
    text-decoration: none;
  }
  .slider-prev {
    position: absolute;
    left: 2px;
    top: 206px;
    width: 40px;
    height: 36px;
    background: var(--nav-grey);
    border: 3px solid var(--cream-light);
    border-left: none;
    display: flex;
    align-items: center;
    justify-content: center;
  }
  .photo-frame {
    position: absolute;
    left: 0;
    top: 0;
  }
</style>
</head>
<body>
  <section class="hero-banner">
    <div class="decor-circle"></div>

    <div class="hero-copy">
      <h1 class="hero-headline">We offer a way of solving<br>family law disputes by<br>offering mediation and<br>arbitration</h1>
      <a class="cta-button" href="#">Get Started</a>
    </div>

    <a class="slider-prev" href="#" aria-label="Previous slide">
      <svg width="12" height="16" viewBox="0 0 12 16">
        <path d="M9 2 L3 8 L9 14" fill="none" stroke="#ffffff" stroke-width="3"/>
      </svg>
    </a>

    <svg class="photo-frame" width="1200" height="450" viewBox="0 0 1200 450">
      <defs>
        <linearGradient id="photoTone" gradientUnits="userSpaceOnUse" x1="490" y1="0" x2="1200" y2="450">
          <stop offset="0" stop-color="var(--photo-light)"/>
          <stop offset="0.55" stop-color="var(--photo-mid)"/>
          <stop offset="1" stop-color="var(--photo-warm)"/>
        </linearGradient>
      </defs>
      <g role="img" aria-label="Smiling family of four – parents with two young sons – in a bright kitchen among moving boxes">
        <circle cx="754" cy="240" r="262" fill="url(#photoTone)"/>
        <rect x="754" y="0" width="446" height="450" fill="url(#photoTone)"/>
      </g>
      <circle cx="754" cy="240" r="271" fill="none" stroke="var(--ring-blue)" stroke-width="18"/>
    </svg>
  </section>
</body>
</html>
```